Business Card Design Project

We have a logo, but would like to expand the use of it into a business card design. We are a B2B technology exchange platform for institutional investors to invest excess cash into short term assets matching their credit and pricing parameters. The assets are fractionalized and investors invest in portions.

Our customers are large, institutional, financial companies who are a bit traditional. We are high energy rebels with a cause...we are a disruptive technology and want to be viewed as a game changer but we need to present an image of trustworthiness and secure.

We are open not only to the image design but the material, die cut, etc. but want to stay in the traditional size of a business card.

We have other formats of the logo if needed. Our website is www.brambleharbor.com

I have posted a powerpoint template that we have been using.  This should not be considered the template we will use (after business cards we will have another project to incorporate business card design into powerpoint template) but just to give you a flavor of where we have been and have used in the past.

Target Market(s)

Institutional investors, asset managers, large fund institutions

Industry/Entity Type

Financial

Requirements
Must have
• Our logo
Traditional size
Nice to have
• unique use of logo, unique material, die cut, etc
Crisp, clean look
Use of both sides of card in a creative manner

```html
<!DOCTYPE html>
<html lang="en">
<head>
<meta charset="utf-8">
<title>Bramble Harbor – Business Card</title>
<link href="https://fonts.googleapis.com/css2?family=Montserrat:wght@400;800&display=swap" rel="stylesheet">
<style>
  :root {
    --orange: #f39200;
    --slate: #58585a;
    --paper: #ffffff;
    --ink: #4a4a4c;
    --backdrop: #2e2e30;
  }
  * { margin: 0; padding: 0; box-sizing: border-box; }
  html, body {
    width: 1200px; height: 715px; overflow: hidden;
    background: var(--backdrop);
    font-family: "Montserrat", sans-serif;
  }
  .sheet {
    position: relative; width: 1200px; height: 715px;
    display: flex; align-items: center; justify-content: center; gap: 60px;
  }
  .card {
    position: relative; width: 525px; height: 300px; overflow: hidden;
  }
  /* Front */
  .card--front { background: var(--orange); }
  .card--front .wordmark {
    position: absolute; left: 205px; top: 118px;
    display: flex; align-items: center; gap: 12px;
  }
  .wordmark__name {
    font-weight: 800; color: var(--slate); letter-spacing: -0.5px;
    line-height: 1;
  }
  .card--front .wordmark__name { font-size: 40px; }
  .wordmark__dot {
    border-radius: 50%; flex: none;
  }
  .card--front .wordmark__dot { width: 28px; height: 28px; background: var(--paper); }

  /* Back */
  .card--back { background: var(--paper); }
  .card--back .wordmark {
    position: absolute; right: 36px; top: 62px;
    display: flex; align-items: center; gap: 8px;
  }
  .card--back .wordmark__name { font-size: 26px; }
  .card--back .wordmark__dot { width: 18px; height: 18px; background: var(--orange); }

  .contact { position: absolute; left: 34px; top: 66px; color: var(--ink); }
  .contact__name { font-size: 19px; font-weight: 400; }
  .contact__title { font-size: 10px; margin-top: 3px; }
  .contact__list { list-style: none; margin-top: 12px; }
  .contact__item {
    display: flex; align-items: center; gap: 8px;
    font-size: 12px; line-height: 18px;
  }
  .contact__icon { width: 13px; height: 13px; flex: none; }
  .contact__web { color: var(--orange); font-size: 12px; margin-top: 4px; }
  .address-band {
    position: absolute; left: 0; right: 0; bottom: 0; height: 36px;
    background: var(--orange); color: var(--paper);
    font-size: 12px; display: flex; align-items: center; padding-left: 34px;
  }
</style>
</head>
<body>
<main class="sheet">
  <section class="card card--front" aria-label="Card front">
    <div class="wordmark">
      <span class="wordmark__dot"></span>
      <span class="wordmark__name">Bramble Harbor</span>
    </div>
  </section>

  <section class="card card--back" aria-label="Card back">
    <div class="contact">
      <p class="contact__name">Evan Marlowe</p>
      <p class="contact__title">President &amp; CEO</p>
      <ul class="contact__list">
        <li class="contact__item">
          <svg class="contact__icon" viewBox="0 0 14 14"><circle cx="7" cy="7" r="7" fill="#f39200"/><path d="M4.5 3.5h1.5l.7 2-1 .7a5 5 0 0 0 2.1 2.1l.7-1 2 .7v1.5c0 .5-.4.8-.9.8A6 6 0 0 1 3.7 4.4c0-.5.3-.9.8-.9z" fill="#fff"/></svg>
          805.555.0142
        </li>
        <li class="contact__item">
          <svg class="contact__icon" viewBox="0 0 14 14"><circle cx="7" cy="7" r="7" fill="#f39200"/><rect x="5" y="3" width="4" height="8" rx="0.8" fill="#fff"/></svg>
          818.555.0179
        </li>
        <li class="contact__item">
          <svg class="contact__icon" viewBox="0 0 14 14"><circle cx="7" cy="7" r="7" fill="#f39200"/><rect x="3.5" y="4.5" width="7" height="5" fill="#fff"/><path d="M3.5 4.5 7 7.3l3.5-2.8" stroke="#f39200" stroke-width="0.8" fill="none"/></svg>
          evanmarlowe@brambleharbor.com
        </li>
        <li class="contact__item">
          <svg class="contact__icon" viewBox="0 0 14 14"><circle cx="7" cy="7" r="7" fill="#f39200"/></svg>
          evan.marlowe
        </li>
      </ul>
      <p class="contact__web">www.brambleharbor.com</p>
    </div>

    <div class="wordmark">
      <span class="wordmark__dot"></span>
      <span class="wordmark__name">Bramble Harbor</span>
    </div>

    <div class="address-band">2210 Fernhollow Drive, Suite 118, Oak Terrace, CA 91450</div>
  </section>
</main>
</body>
</html>
```